Business Card Design Project

I am looking for a minimal matte background/shiny (spot UV) ink monochromatic design with a splash of neon color.

the card should be 2 sided, logo only on one side - all info and possibly logo on the other.

My creative director described the colors he imagined for the design to be:
'it's a dark field, like charcoal or a really dark burgundy, or deep blue, shot through with a neon—but just a tiny bit of it. so a charcoal field with a laser-thin streak of electric lime, safety orange, or cobalt blue. really beautiful stuff.'

here are some samples of the types of cards I am trying to create:
http://www.pictavault.example/photos/dawnpress/6967376935/in/photostream -> Vandrelle Lustre

http://www.pictavault.example/photos/dawnpress/6497659409/in/photostream -> Standard Coated (14pt/matte) with SPOT UV

http://www.pictavault.example/photos/dawnpress/6497658995/in/photostream/ -> Heavy Corvane with Raised Ink

http://www.pictavault.example/photos/dawnpress/6275629165/in/photostream/ -> Standard Coated (14pt/matte) with SPOT UV

Here is my logo:
https://www.filecrate.example/s/sigym192mlh58ge/quillorb%20logotype%20final.ai

Here are the details for info:
Dorian Elwood Marsh
email - dorian@quillorb.example
mobile - 555 013 2867
web -
quillorb.example: inventive technology applications
quillorb-tv.example: innovative video advertising

please let me know if there is anything at all that you need.

Target Market(s)

mid to large agencies that require interactive design and entrepreneurial/startup individuals/companies that need application development.

Industry/Entity Type

Safety

Requirements
Must have
• logo only on one side

```html
<!DOCTYPE html>
<html lang="en">
<head>
<meta charset="utf-8">
<title>Quillorb business card — front and back</title>
<link rel="stylesheet" href="https://fonts.googleapis.com/css2?family=Oswald:wght@400&family=Lexend:wght@300;600&display=swap">
<style>
  :root {
    --backdrop: #1b1c1f;
    --card-top: #21479a;
    --card-bottom: #132c69;
    --silver: #e4e6ec;
    --ink-white: #ffffff;
    --rule: rgba(190, 205, 235, 0.45);
    --arrow: #9fb0cf;
  }
  * { margin: 0; padding: 0; box-sizing: border-box; }
  html, body {
    width: 1200px; height: 1200px; overflow: hidden;
    background: var(--backdrop);
  }
  .canvas { position: relative; width: 1200px; height: 1200px; }

  .card {
    position: absolute; left: 150px;
    width: 900px; height: 514px;
    background: linear-gradient(170deg, var(--card-top) 0%, var(--card-bottom) 100%);
    box-shadow: 0 10px 30px rgba(0,0,0,0.55);
    overflow: hidden;
  }
  .card--front { top: 57px; }
  .card--back  { top: 628px; }

  .wordmark {
    position: absolute;
    font-family: "Oswald", "Arial Narrow", sans-serif;
    font-weight: 400;
    color: var(--silver);
    text-transform: uppercase;
    white-space: nowrap;
  }
  .card--front .wordmark {
    left: 0; right: 0; top: 196px;
    text-align: center;
    font-size: 84px; letter-spacing: 22px; line-height: 1;
    padding-left: 22px;
  }
  .wordmark-dot {
    position: absolute; left: 742px; top: 178px;
    width: 18px; height: 18px; border-radius: 50%;
    background: var(--silver);
  }

  .card--back .wordmark {
    left: 0; width: 970px; top: 72px; text-align: center;
    font-size: 24px; letter-spacing: 6px; line-height: 1;
  }
  .holder-name {
    position: absolute; left: 0; width: 970px; top: 102px;
    text-align: center;
    font-family: "Lexend", sans-serif; font-weight: 600;
    font-size: 34px; color: var(--ink-white); letter-spacing: 0.5px;
  }
  .name-rule {
    position: absolute; left: 330px; top: 154px; width: 310px; height: 2px;
    background: linear-gradient(90deg, transparent, var(--rule) 20%, var(--rule) 80%, transparent);
  }
  .divider {
    position: absolute; left: 440px; top: 230px; width: 1px; height: 150px;
    background: var(--rule);
  }

  .contact {
    position: absolute; left: 48px;
    font-family: "Lexend", sans-serif; font-weight: 300;
    font-size: 25px; color: var(--ink-white);
    display: flex; align-items: center; gap: 16px;
  }
  .contact--email { top: 300px; }
  .contact--phone { top: 342px; }
  .contact strong { font-weight: 600; }

  .site {
    position: absolute; left: 474px;
    font-family: "Lexend", sans-serif; color: var(--ink-white);
  }
  .site-domain { font-weight: 600; font-size: 23px; }
  .site-desc { font-weight: 300; font-size: 23px; }
  .site--one-domain { top: 228px; }
  .site--one-desc   { top: 275px; }
  .site--two-domain { top: 300px; }
  .site--two-desc   { top: 345px; }

  .arrow { position: absolute; }
</style>
</head>
<body>
<main class="canvas">

  <section class="card card--front" aria-label="Card front">
    <div class="wordmark">Quillorb</div>
    <span class="wordmark-dot"></span>
  </section>

  <section class="card card--back" aria-label="Card back">
    <div class="wordmark">Quillorb</div>
    <h1 class="holder-name">Dorian Elwood Marsh</h1>
    <div class="name-rule"></div>

    <div class="contact contact--email">
      <svg width="32" height="22" viewBox="0 0 32 22" aria-hidden="true">
        <rect x="1" y="1" width="30" height="20" fill="#fff"/>
        <path d="M1 1 L16 12 L31 1" fill="none" stroke="#1a3a80" stroke-width="2"/>
      </svg>
      <span>dorian@quillorb.example</span>
    </div>
    <div class="contact contact--phone">
      <svg width="32" height="30" viewBox="0 0 32 30" aria-hidden="true">
        <rect x="7" y="1" width="18" height="28" rx="3" fill="none" stroke="#fff" stroke-width="2"/>
        <line x1="7" y1="23" x2="25" y2="23" stroke="#fff" stroke-width="2"/>
        <circle cx="16" cy="26" r="1.2" fill="#fff"/>
      </svg>
      <span><strong>+555</strong> 013 2867</span>
    </div>

    <div class="divider"></div>

    <div class="site site--one-domain site-domain">quillorb.example</div>
    <svg class="arrow" style="left:640px;top:262px" width="40" height="30" viewBox="0 0 40 30" aria-hidden="true">
      <path d="M2 3 Q26 2 30 24" fill="none" stroke="var(--arrow)" stroke-width="1.5"/>
      <path d="M25 19 L30 25 L34 18" fill="none" stroke="var(--arrow)" stroke-width="1.5"/>
    </svg>
    <div class="site site--one-desc site-desc">inventive technology applications</div>

    <div class="site site--two-domain site-domain">quillorb-tv.example</div>
    <svg class="arrow" style="left:448px;top:318px" width="26" height="48" viewBox="0 0 26 48" aria-hidden="true">
      <path d="M22 46 Q4 40 8 6" fill="none" stroke="var(--arrow)" stroke-width="1.5"/>
      <path d="M3 12 L8 5 L13 11" fill="none" stroke="var(--arrow)" stroke-width="1.5"/>
    </svg>
    <div class="site site--two-desc site-desc">innovative video advertising</div>
  </section>

</main>
</body>
</html>
```